Letter and Envelope Design For Larchmont Realty

Please design a letter and an envelope incorporating our logo (See Attached). We are also launched a business card contest. Since we want them to match, please feel free to submit a design for both the business card and also the letter design and envelope.

Requirements
Must have
• The envelope, the letter and the business cards must match somehow connecting the designs. We want them to have something that holds them together besides the logo.

```html
<!DOCTYPE html>
<html lang="en">
<head>
<meta charset="utf-8">
<title>Larchmont Realty – Stationery Set</title>
<link rel="stylesheet" href="https://fonts.googleapis.com/css2?family=Montserrat:wght@600&family=Work+Sans:wght@400&display=swap">
<style>
  :root{
    --navy:#27307f;
    --navy-soft:#323b8e;
    --navy-dark:#222a72;
    --charcoal:#555555;
    --body-grey:#6b6b6b;
    --backdrop:#ebebeb;
    --paper:#ffffff;
  }
  *{margin:0;padding:0;box-sizing:border-box}
  html,body{width:1200px;height:762px;overflow:hidden;background:var(--backdrop)}
  .canvas{position:relative;width:1200px;height:762px}
  .sheet{position:absolute;background:var(--paper);overflow:hidden;box-shadow:0 2px 6px rgba(0,0,0,.18)}

  .letterhead{left:45px;top:52px;width:466px;height:658px}
  .business-card{left:549px;top:52px;width:606px;height:302px}
  .envelope{left:549px;top:408px;width:606px;height:302px;background:var(--navy)}

  .footer-band{position:absolute;left:0;right:0;bottom:0;background:linear-gradient(180deg,var(--navy-soft),var(--navy))}
  .letterhead .footer-band{top:550px}
  .business-card .footer-band{top:150px}

  .wordmark{position:absolute;font-family:"Montserrat",sans-serif;font-weight:600;color:var(--navy);text-align:center;line-height:1}
  .wordmark .line-1{display:block;font-size:26px;letter-spacing:3.4px}
  .wordmark .line-2{display:block;font-size:19px;letter-spacing:7px;margin-top:6px}
  .letterhead .wordmark{left:0;width:466px;top:27px}
  .business-card .wordmark{left:26px;top:27px;width:250px}

  .emblem{position:absolute;border-radius:50%;background:var(--paper);border:5px solid var(--navy);
    display:flex;align-items:center;justify-content:center;
    font-family:"Montserrat",sans-serif;font-weight:600;color:var(--charcoal);line-height:1.25;text-align:center}
  .letterhead .emblem{left:329px;top:438px;width:116px;height:116px;font-size:11.5px;letter-spacing:1px}
  .business-card .emblem{left:428px;top:21px;width:148px;height:148px;font-size:14.5px;letter-spacing:1.2px}

  .letter-body{position:absolute;left:32px;top:182px;width:408px;font-family:"Work Sans",sans-serif;color:var(--body-grey)}
  .salutation{position:absolute;left:32px;top:131px;font-family:"Work Sans",sans-serif;font-size:13px;color:var(--navy)}
  .letter-body p.copy{font-size:9.1px;line-height:12.2px;letter-spacing:-.05px;margin-bottom:15px}
  .sign-off{position:absolute;left:32px;top:457px;font-family:"Work Sans",sans-serif;font-size:10.5px;color:#444}
  .signature-area{position:absolute;left:32px;top:478px;width:84px;height:13px;background:linear-gradient(90deg,#d9d9d9,#ececec);border-radius:3px}

  .contact{position:absolute;font-family:"Work Sans",sans-serif;font-style:normal;color:#fff;text-align:right}
  .contact .address{display:block}
  .contact .row{display:flex;justify-content:flex-end;align-items:center;gap:5px}
  .contact svg{flex:none}
  .letterhead .contact{right:31px;top:573px;font-size:8.6px;line-height:12px}
  .letterhead .contact .channels{margin-top:7px}
  .business-card .contact{right:33px;top:196px;font-size:11px;line-height:15.5px}
  .business-card .contact .channels{margin-top:8px}

  .envelope .flap{position:absolute;inset:0}
  .envelope .seal{position:absolute;left:272px;top:151px;width:62px;height:62px;border-radius:50%;border:4px solid #fff}
  .envelope .wordmark{left:0;width:606px;top:224px;color:#fff}
  .envelope .wordmark .line-1{font-size:17px;letter-spacing:2.4px}
  .envelope .wordmark .line-2{font-size:13.5px;letter-spacing:5px;margin-top:4px}
</style>
</head>
<body>
<main class="canvas">

  <section class="sheet letterhead">
    <div class="footer-band" role="img" aria-label="Navy decorative footer band"></div>
    <div class="wordmark"><span class="line-1">LARCHMONT</span><span class="line-2">REALTY</span></div>
    <p class="salutation">Dear Sir</p>
    <div class="letter-body">
      <p class="copy">Lorem ipsum dolor sit amet, an vel recteque dissentiet, detracto albucius platonem ex vel, eros repudiandae cu. Atqui aliquando nec an, unum graece adolescens vel ad. Id odio scae has, iudico euismod atomorum ius ea, cum ea honestatis quaerendum theophrastus. Mea honestatis quaerendum theophrastus. Mea</p>
      <p class="copy">Lorem ipsum dolor sit amet, an vel recteque dissentiet, detracto albucius platonem ex vel, eros repudiandae cu. Atqui aliquando nec an, unum graece adolescens vel ad. Id odio scae has, iudico euismod atomorum ius ea, cum ea honestatis quaerendum theophrastus. Mea doming repudiandae ex, cu cum civibus assentior posidonium. Quo etiam pertinax ex, te eros repudiandae cu. Atqui aliquando nec an, unum graece adolescens vel ad. Id odio scae honestatis quaerendum theophrastus. Mea</p>
      <p class="copy">Lorem ipsum dolor sit amet, an vel recteque dissentiet, detracto albucius platonem ex vel, eros repudiandae cu. Atqui aliquando nec an, unum graece adolescens vel ad. Id odio scae has, iudico euismod atomorum ius ea, cum ea honestatis quaerendum theophrastus. Mea honestatis quaerendum theophrastus. Mea</p>
      <p class="copy">Lorem ipsum dolor sit amet, an vel recteque dissentiet, detracto albucius platonem ex vel, eros repudiandae cu. Atqui aliquando nec an, unum graece adolescens vel ad. Id odio scae has, iudico euismod atomorum ius ea, cum ea honestatis quaerendum theophrastus. Mea honestatis quaerendum theophrastus. Mea</p>
    </div>
    <p class="sign-off">Kind Regards</p>
    <div class="signature-area" role="img" aria-label="Handwritten signature of the sender"></div>
    <div class="emblem">LARCHMONT<br>REALTY</div>
    <address class="contact">
      <span class="address">48b Harlow Street,</span>
      <span class="address">Wellford, NZ, 7022</span>
      <div class="channels">
        <div class="row">(555) 014-2287 <svg width="7" height="7" viewBox="0 0 10 10"><path d="M2,1 L4,1 L5,3.5 L3.8,4.5 Q5,6.5 6,6.5 L7,5.2 L9,6.2 L9,8.5 Q3,9 1,2 Z" fill="#fff"/></svg></div>
        <div class="row">info@larchmontrealty.com <svg width="7" height="7" viewBox="0 0 10 10"><rect x="1" y="2.5" width="8" height="5.5" fill="none" stroke="#fff" stroke-width="1.2"/><path d="M1,2.5 L5,5.5 L9,2.5" fill="none" stroke="#fff" stroke-width="1"/></svg></div>
        <div class="row">www.larchmontrealty.com <svg width="7" height="7" viewBox="0 0 10 10"><circle cx="5" cy="5" r="4" fill="none" stroke="#fff" stroke-width="1.2"/><path d="M1,5 H9 M5,1 V9" stroke="#fff" stroke-width=".8"/></svg></div>
      </div>
    </address>
  </section>

  <section class="sheet business-card">
    <div class="footer-band" role="img" aria-label="Navy decorative footer band"></div>
    <div class="wordmark"><span class="line-1">LARCHMONT</span><span class="line-2">REALTY</span></div>
    <div class="emblem">LARCHMONT<br>REALTY</div>
    <address class="contact">
      <span class="address">48b Harlow Street,</span>
      <span class="address">Wellford, NZ, 7022</span>
      <div class="channels">
        <div class="row">(555) 014-2287 <svg width="8" height="8" viewBox="0 0 10 10"><path d="M2,1 L4,1 L5,3.5 L3.8,4.5 Q5,6.5 6,6.5 L7,5.2 L9,6.2 L9,8.5 Q3,9 1,2 Z" fill="#fff"/></svg></div>
        <div class="row">info@larchmontrealty.com <svg width="8" height="8" viewBox="0 0 10 10"><rect x="1" y="2.5" width="8" height="5.5" fill="none" stroke="#fff" stroke-width="1.2"/><path d="M1,2.5 L5,5.5 L9,2.5" fill="none" stroke="#fff" stroke-width="1"/></svg></div>
        <div class="row">www.larchmontrealty.com <svg width="8" height="8" viewBox="0 0 10 10"><circle cx="5" cy="5" r="4" fill="none" stroke="#fff" stroke-width="1.2"/><path d="M1,5 H9 M5,1 V9" stroke="#fff" stroke-width=".8"/></svg></div>
      </div>
    </address>
  </section>

  <section class="sheet envelope">
    <svg class="flap" width="606" height="302" viewBox="0 0 606 302" aria-hidden="true">
      <path d="M0,0 L606,0 L594,62 Q588,94 552,95 L54,95 Q18,94 12,62 Z" fill="var(--navy-dark)"/>
      <path d="M12,62 Q18,94 54,95 L552,95 Q588,94 594,62" fill="none" stroke="rgba(0,0,0,.22)" stroke-width="2"/>
    </svg>
    <div class="seal"></div>
    <div class="wordmark"><span class="line-1">LARCHMONT</span><span class="line-2">REALTY</span></div>
  </section>

</main>
</body>
</html>
```